Furniture restoration to chairs. Hand weaving.

Industry/Entity Type

Furniture

Contact Information for Business Card

The Reed Loom
Cane, rush, splint and shaker tape.
58 Tolan Rd
Fenwick Cove
ME 04583
207 - 512 - 3087
Cell: 207 - 834 - 2719

For graphics I want a picture of a caned rocking chair or maybe a rush and a cane chair.

```html
<!DOCTYPE html>
<html lang="en">
<head>
<meta charset="utf-8">
<title>The Reed Loom — Business Card</title>
<link rel="stylesheet" href="https://fonts.googleapis.com/css2?family=PT+Sans:wght@400;700&display=swap">
<style>
  :root {
    --brand-blue: #1473bd;
    --brand-blue-deep: #0f62a6;
    --ink: #1d1d1f;
    --card-white: #ffffff;
    --ice: #e6f2fb;
    --ice-deep: #bfdcf2;
    --backdrop: #eceef0;
    --chair-blue: #1f4f86;
    --chair-rush: #c48a52;
  }
  * { margin: 0; padding: 0; box-sizing: border-box; }
  html, body {
    width: 1200px;
    height: 800px;
    overflow: hidden;
    background: var(--backdrop);
  }
  .canvas {
    position: relative;
    width: 1200px;
    height: 800px;
  }
  .card {
    position: absolute;
    left: 50px;
    top: 40px;
    width: 1100px;
    height: 720px;
    overflow: hidden;
    background:
      linear-gradient(135deg, transparent 55%, rgba(191, 220, 242, 0.55) 100%),
      linear-gradient(200deg, var(--ice) 0%, var(--card-white) 45%, var(--ice) 100%);
    box-shadow: 0 6px 22px rgba(0, 0, 0, 0.12);
  }
  .card__facets,
  .card__wave {
    position: absolute;
    inset: 0;
    width: 1100px;
    height: 720px;
  }
  .card__photo {
    position: absolute;
    left: 640px;
    top: 70px;
    width: 300px;
    height: 420px;
    border-radius: 6px;
    background: linear-gradient(180deg, var(--chair-blue) 0%, var(--chair-blue) 40%, var(--chair-rush) 55%, var(--chair-blue) 100%);
    opacity: 0.85;
  }
  .identity {
    position: absolute;
    left: 170px;
    top: 395px;
    font-family: "PT Sans", sans-serif;
    color: var(--brand-blue);
  }
  .identity__name {
    font-size: 66px;
    font-weight: 700;
    line-height: 1;
    letter-spacing: -0.5px;
  }
  .identity__tagline {
    font-size: 26px;
    font-weight: 400;
    margin-top: 6px;
  }
  .contact {
    position: absolute;
    left: 170px;
    top: 505px;
    list-style: none;
    font-family: "PT Sans", sans-serif;
    color: var(--ink);
    font-size: 40px;
    line-height: 1.3;
  }
  .contact__item {
    display: flex;
    align-items: center;
    gap: 14px;
  }
  .contact__icon {
    width: 30px;
    height: 30px;
    fill: var(--brand-blue);
    flex: none;
  }
</style>
</head>
<body>
<main class="canvas">
  <section class="card">
    <svg class="card__facets" viewBox="0 0 1100 720" aria-hidden="true">
      <polygon points="560,720 820,380 1100,520 1100,720" fill="#d4e9f8" opacity="0.6"/>
      <polygon points="300,720 620,420 760,720" fill="#e2f0fa" opacity="0.7"/>
      <polygon points="820,380 1100,200 1100,520" fill="#cde4f5" opacity="0.5"/>
      <polygon points="0,560 220,720 0,720" fill="#d8ebf8" opacity="0.6"/>
    </svg>

    <svg class="card__wave" viewBox="0 0 1100 720" aria-hidden="true">
      <path d="M0,0 H1100 V30 C820,45 620,110 430,215 C280,295 130,330 0,335 Z" fill="var(--brand-blue)"/>
      <path d="M1100,48 C830,62 640,130 455,235 C300,320 150,365 0,372 V345 C145,342 290,305 440,222 C630,115 830,55 1100,40 Z" fill="var(--card-white)"/>
      <path d="M1100,60 C840,72 650,145 470,250 C310,345 160,395 0,405 V375 C150,368 300,325 455,240 C640,135 835,68 1100,52 Z" fill="var(--brand-blue-deep)"/>
    </svg>

    <div class="card__photo" role="img" aria-label="Photograph of a painted blue wooden chair with a hand-woven rush seat"></div>

    <header class="identity">
      <h1 class="identity__name">The Reed Loom</h1>
      <p class="identity__tagline">Cane, rush, splint and shaker tape.</p>
    </header>

    <ul class="contact">
      <li class="contact__item">
        <svg class="contact__icon" viewBox="0 0 24 24" aria-hidden="true"><path d="M12 3 2 12h3v8h5v-5h4v5h5v-8h3z"/></svg>
        <span>58 Tolan Rd Fenwick Cove ME 04583</span>
      </li>
      <li class="contact__item">
        <svg class="contact__icon" viewBox="0 0 24 24" aria-hidden="true"><path d="M3 9c0-3 4-5 9-5s9 2 9 5v2h-5V9c-1-.6-2.4-1-4-1s-3 .4-4 1v2H3zM6 13h12l2 7H4z"/></svg>
        <span>207 - 512 - 3087</span>
      </li>
      <li class="contact__item">
        <svg class="contact__icon" viewBox="0 0 24 24" aria-hidden="true"><path d="M7 2h10a2 2 0 0 1 2 2v16a2 2 0 0 1-2 2H7a2 2 0 0 1-2-2V4a2 2 0 0 1 2-2zm0 3v12h10V5zm5 13.5a1.2 1.2 0 1 0 0 2.4 1.2 1.2 0 0 0 0-2.4z"/></svg>
        <span>207 - 834 - 2719</span>
      </li>
    </ul>
  </section>
</main>
</body>
</html>
```